Website Page Design for Velmont Microbrewery

We need a website page design for our brewery based on our logo and label.

Industry/Entity Type

Brewery

```html
<!DOCTYPE html>
<html lang="en">
<head>
<meta charset="utf-8">
<title>Velmont Microbrewery</title>
<link rel="stylesheet" href="https://fonts.googleapis.com/css2?family=Arimo:wght@400;700&family=Noto+Serif:ital,wght@0,400;0,700;1,400&family=Oswald:wght@400&family=Open+Sans:wght@300&display=swap">
<style>
:root{
  --paper:#ece4d1;
  --paper-dark:#e2d8c2;
  --ink:#3b342c;
  --maroon:#6e1026;
  --teal:#1d5a66;
  --nav:#1e1d1c;
  --nav-active:#b47726;
  --white:#ffffff;
  --rule:#cfc4ae;
  --label:#141414;
}
*{margin:0;padding:0;box-sizing:border-box}
html,body{width:1200px;height:2647px;overflow:hidden}
body{background:radial-gradient(ellipse at 50% 20%,#f1eadb 0%,var(--paper) 55%,var(--paper-dark) 100%);font-family:"Noto Serif",Georgia,serif;color:var(--ink);position:relative}
.abs{position:absolute}
a{color:var(--teal);font-style:italic}
.brand{left:106px;top:52px;display:flex;align-items:center;gap:14px;font-family:"Noto Serif",Georgia,serif;font-weight:700;font-size:58px;color:var(--label)}
.brand-dot{width:22px;height:22px;border-radius:50%;background:var(--nav-active)}
.latest{left:476px;top:36px;width:330px}
.latest h3{font-family:"Arimo",Arial,sans-serif;font-weight:400;font-size:21px;color:#9b6a1f;margin-bottom:10px}
.latest a{display:block;font-size:13.5px;line-height:22px;color:#4b3a2c}
.search{left:856px;top:42px;width:233px;height:39px;background:var(--white);border-radius:3px;box-shadow:0 1px 3px rgba(0,0,0,.18);font-style:italic;font-size:15px;color:#999;padding:10px 14px}
.search svg{position:absolute;right:10px;top:11px}
.search::after{content:"";position:absolute;right:36px;top:8px;bottom:8px;width:1px;background:#ddd}
.tagline{left:846px;top:104px;width:243px;text-align:right;font-style:italic;font-size:13.5px;line-height:20px}
.nav{left:101px;top:214px;width:990px;height:67px;background:linear-gradient(#2d2b29,var(--nav));border-radius:3px 3px 0 0;display:flex;align-items:stretch;padding-left:18px}
.nav a{font-family:"Oswald",Arial,sans-serif;font-style:normal;font-size:18px;letter-spacing:.5px;color:#e8e2d6;text-decoration:none;display:flex;align-items:center;padding:0 32px;position:relative}
.nav a.active{background:linear-gradient(#c58a35,var(--nav-active))}
.nav a.sep::before{content:"";position:absolute;left:-2px;top:31px;width:5px;height:5px;border-radius:50%;background:#b2283b}
.hero{left:101px;top:281px;width:990px;height:291px;background:linear-gradient(180deg,#c88068 0%,#8d6d6a 30%,#6b6c3a 50%,#3c4a1d 80%,#2c3516 100%)}
.hero-title{left:575px;top:406px;height:70px;padding:0 22px;background:rgba(0,0,0,.55);font-family:"Open Sans",Arial,sans-serif;font-weight:300;font-size:50px;line-height:70px;color:var(--white)}
.hero-sub{left:547px;top:476px;height:24px;padding:0 16px;background:rgba(0,0,0,.7);font-style:italic;font-size:14px;line-height:24px;color:#ddd}
.pager{font-family:"Arimo",Arial,sans-serif;font-size:10px;color:#555;text-align:center;width:40px}
.tile{width:279px;height:159px;border:2px solid var(--white);box-shadow:0 1px 3px rgba(0,0,0,.2)}
.tile-label{position:absolute;top:0;background:var(--label);color:var(--white);font-family:"Arimo",Arial,sans-serif;font-size:22px;line-height:30px;padding:0 8px;display:flex;align-items:center;gap:8px}
.tile-label.right{right:0}
.tile-label.left{left:0}
.play-dot{width:18px;height:18px;border-radius:50%;background:var(--white);display:inline-flex;align-items:center;justify-content:center}
.count{position:absolute;width:24px;height:24px;border-radius:50%;background:var(--label);color:var(--white);font-family:"Arimo",Arial,sans-serif;font-weight:700;font-size:10px;line-height:24px;text-align:center}
.tile .count{bottom:6px}
.tile .count.r{right:6px}
.tile .count.l{left:6px}
.feature{left:386px;top:625px;width:416px;height:492px;background:var(--white);box-shadow:0 1px 3px rgba(0,0,0,.15)}
.feature-img{left:18px;top:18px;width:380px;height:270px;background:linear-gradient(180deg,#b98134 0%,#6b3a17 55%,#2c1a10 100%)}
.feature h2{position:absolute;left:30px;top:314px;font-family:"Arimo",Arial,sans-serif;font-weight:400;font-size:28px;color:var(--maroon);display:flex;align-items:center;gap:12px}
.feature h2 .count{position:static}
.feature p{position:absolute;left:32px;top:362px;width:355px;font-style:italic;font-size:14.5px;line-height:22px}
.more{left:101px;top:1146px;width:990px;height:20px}
.more::before{content:"";position:absolute;left:0;right:0;top:10px;height:1px;background:var(--rule)}
.more span{position:absolute;left:460px;top:0;padding:0 14px;background:var(--paper);font-style:italic;font-size:15px;color:#666}
.section-title{font-family:"Arimo",Arial,sans-serif;font-weight:400;font-size:28px;color:var(--maroon)}
.video{left:101px;top:1255px;width:679px;height:418px;background:var(--white);padding:8px;box-shadow:0 1px 3px rgba(0,0,0,.2)}
.video-img{width:100%;height:100%;background:radial-gradient(ellipse at 50% 55%,#d9c53a 0%,#8a7a3a 25%,#3c3d44 60%,#1d2230 100%);position:relative}
.play{position:absolute;left:331px;top:200px;width:80px;height:80px;border-radius:6px;background:linear-gradient(#f4f4f4,#cfcfcf);display:flex;align-items:center;justify-content:center}
.body-text{font-size:14.5px;line-height:22px;width:679px}
.meta{display:flex;align-items:center;font-size:14px;gap:8px}
.meta .count{position:static;background:#24545c}
.meta .tags{margin-left:30px;color:#555}
.meta .share{margin-left:30px;color:#555;display:flex;gap:6px;align-items:center}
.sq{display:inline-block;width:18px;height:18px;border-radius:3px}
.deal-img{left:109px;top:1941px;width:291px;height:194px;border:5px solid var(--white);box-shadow:0 1px 3px rgba(0,0,0,.2);background:linear-gradient(90deg,#5a2a16 0%,#c66a1d 45%,#e0a33a 70%,#8c3a18 100%)}
.side-title{font-family:"Arimo",Arial,sans-serif;font-size:20px;color:var(--maroon)}
.subscribe{left:844px;top:1249px;width:246px;height:41px;background:var(--white);border-radius:3px;box-shadow:0 1px 3px rgba(0,0,0,.18);font-style:italic;font-size:14px;color:#999;padding:11px 16px}
.subscribe svg{position:absolute;right:10px;top:13px}
.subscribe::after{content:"";position:absolute;right:38px;top:8px;bottom:8px;width:1px;background:#ddd}
.social{width:53px;text-align:center}
.social .box{width:36px;height:30px;margin:0 auto;border-radius:3px}
.social .num{margin-top:2px;background:var(--white);border:1px solid #ccc;border-radius:3px;font-family:"Arimo",Arial,sans-serif;font-size:13px;color:#444;line-height:20px}
.popular{left:844px;top:1468px;width:250px}
.popular a{display:block;font-size:13.5px;line-height:20px;margin-bottom:4px}
.bubble{left:847px;top:1775px;width:230px;height:230px;border-radius:50%;background:radial-gradient(circle at 50% 40%,#3a3a3a,#0e0e0e 75%);color:var(--white);text-align:center;padding:60px 26px 0}
.bubble p{font-style:italic;font-size:13px;line-height:19px}
.bubble hr{border:none;border-top:1px solid #666;margin:22px 6px 10px}
.bubble a{color:#e0e0e0;font-size:14px}
.bubble-tail{left:880px;top:1770px}
.footer-rule{left:101px;top:2374px;width:990px;height:1px;background:var(--rule)}
.footer-brand{left:106px;top:2470px;display:flex;align-items:center;gap:10px;font-family:"Noto Serif",Georgia,serif;font-weight:700;font-size:34px;color:var(--label)}
.footer-col{top:2440px}
.footer-col h4{font-family:"Arimo",Arial,sans-serif;font-weight:700;font-size:14px;color:var(--maroon);margin-bottom:16px;letter-spacing:.3px}
.footer-col a{display:block;font-size:14.5px;line-height:21px}
</style>
</head>
<body>

<div class="abs brand"><span class="brand-dot"></span>Velmont</div>

<div class="abs latest">
  <h3>Latest articles</h3>
  <a>Lorem ipsum dolor sit amet, consectetur adipisicing elit, sed do eiusmod tempor incididunt ut labore et dolore magna aliqua.</a>
  <a>Lorem ipsum dolor sit amet, consectetur adipisicing elit, sed do eiusmod tempor.</a>
</div>

<div class="abs search">Search
  <svg width="16" height="16" viewBox="0 0 16 16"><circle cx="6.5" cy="6.5" r="4.5" fill="none" stroke="#7a1a2c" stroke-width="2"/><line x1="10" y1="10" x2="14" y2="14" stroke="#7a1a2c" stroke-width="2.5"/></svg>
</div>
<p class="abs tagline">The best blog about beer. We love beer and we can't live without it. See always the latest news and reviews</p>

<nav class="abs nav">
  <a>INÍCIO</a>
  <a class="active">NOSSA HISTÓRIA</a>
  <a>CERVEJAS</a>
  <a class="sep">A CERVEJARIA</a>
  <a class="sep">EVENTOS</a>
  <a class="sep">CONTATO</a>
</nav>

<div class="abs hero" role="img" aria-label="Glass of beer in front of a vineyard road at sunset"></div>
<div class="abs hero-title">Velmont Brewer</div>
<div class="abs hero-sub">Unique resource for beer lovers</div>
<div class="abs pager" style="left:38px;top:380px">
  <svg width="16" height="26" viewBox="0 0 16 26"><polyline points="13,2 3,13 13,24" fill="none" stroke="#555" stroke-width="2"/></svg><br>PREV</div>
<div class="abs pager" style="left:1116px;top:380px">
  <svg width="16" height="26" viewBox="0 0 16 26"><polyline points="3,2 13,13 3,24" fill="none" stroke="#555" stroke-width="2"/></svg><br>NEXT</div>

<!-- left tiles -->
<div class="abs tile" style="left:101px;top:625px;background:linear-gradient(90deg,#3a2114,#a1591d 50%,#5a2e14)" role="img" aria-label="Bartender pouring beer in a restaurant">
  <div class="tile-label right">Monaco restaurants</div><span class="count r">25</span></div>
<div class="abs tile" style="left:101px;top:792px;background:linear-gradient(90deg,#d38a2a,#7a3a18 60%,#3a1c10)" role="img" aria-label="Beer mug next to grilled meat">
  <div class="tile-label right"><span class="play-dot"><svg width="8" height="8" viewBox="0 0 8 8"><polygon points="1,0 8,4 1,8" fill="#141414"/></svg></span>Beer &amp; Meat</div><span class="count r">25</span></div>
<div class="abs tile" style="left:101px;top:958px;background:linear-gradient(90deg,#5a2410,#9a4a16 40%,#c17a2a 75%,#6b3414)" role="img" aria-label="Row of beer glasses with different beers">
  <div class="tile-label right">Best beer deals</div><span class="count r">25</span></div>

<!-- feature -->
<div class="abs feature">
  <div class="abs feature-img" role="img" aria-label="Historic domed cathedral under a golden sky"></div>
  <h2>The spirit of City Name <span class="count">25</span></h2>
  <p>Lorem ipsum dolor sit amet, consectetur adipisicing elit, sed do eiusmod tempor incididunt ut labore et dolore magna aliqua. Lorem ipsum dolor sit amet, consectetur adipisicing elit, sed do eiusmod tempor incididunt ut labore et dolore magna aliqua.</p>
</div>

<!-- right tiles -->
<div class="abs tile" style="left:810px;top:625px;background:linear-gradient(135deg,#f4f2ea,#e8e3d4 50%,#8a5a2a)" role="img" aria-label="Cheese with tomatoes and olive oil">
  <div class="tile-label left">Cheese</div><span class="count l">25</span></div>
<div class="abs tile" style="left:810px;top:792px;background:linear-gradient(90deg,#3a2a1e,#7a5a3a 50%,#d99a2a 75%,#5a3a20)" role="img" aria-label="Glass of lager on a bar">
  <div class="tile-label left"><span class="play-dot"><svg width="8" height="8" viewBox="0 0 8 8"><polygon points="1,0 8,4 1,8" fill="#141414"/></svg></span>Beer Brands</div><span class="count l">25</span></div>
<div class="abs tile" style="left:810px;top:958px;background:linear-gradient(135deg,#4a2a16,#7a5a34 50%,#3a2010)" role="img" aria-label="Hops and roasted malt grains">
  <div class="tile-label left" style="width:279px;line-height:26px;padding:2px 8px">The best raw mate in the world</div><span class="count l">25</span></div>

<div class="abs more"><span>More ⌄</span></div>

<!-- article 1 -->
<h2 class="abs section-title" style="left:101px;top:1192px">Top-10 best beer restaurant in City</h2>
<div class="abs video">
  <div class="video-img" role="img" aria-label="Illuminated stadium at night">
    <div class="play"><svg width="28" height="32" viewBox="0 0 28 32"><polygon points="2,2 26,16 2,30" fill="#555"/></svg></div>
  </div>
</div>
<p class="abs body-text" style="left:101px;top:1702px">Lorem ipsum dolor sit amet, consectetur adipisicing elit, sed do eiusmod tempor incididunt ut labore et dolore magna aliqua. Lorem ipsum dolor sit amet, consectetur adipisicing elit, sed do eiusmod tempor incididunt ut labore et dolore magna aliqua.</p>
<div class="abs meta" style="left:101px;top:1795px">
  <span class="count">25</span><a>comments</a>
  <span class="tags">Tags: <a>Italy</a>, <a>Best beer</a>, <a>Spirit</a>, <a>World championship</a>, <a>Eat</a></span>
  <span class="share">Share: <span class="sq" style="background:#3b5a9a"></span><span class="sq" style="background:#3fa9d6"></span></span>
</div>

<!-- article 2 -->
<h2 class="abs section-title" style="left:101px;top:1873px">Best beer deals</h2>
<div class="abs deal-img" role="img" aria-label="Beer mug with steak and fries"></div>
<p class="abs body-text" style="left:439px;top:1932px;width:340px">Lorem ipsum dolor sit amet, consectetur adipisicing elit, sed do eiusmod tempor incididunt ut labore et dolore magna aliqua. Lorem ipsum dolor sit amet, consectetur adipisicing elit, sed do eiusmod tempor incididunt ut labore et dolore magna aliqua.</p>
<p class="abs body-text" style="left:439px;top:2068px;width:340px">Lorem ipsum dolor sit amet, consectetur adipisicing elit, sed do eiusmod tempor incididunt ut labore et dolore magna aliqua.</p>
<p class="abs body-text" style="left:101px;top:2163px">Lorem ipsum dolor sit amet, consectetur adipisicing elit, sed do eiusmod tempor incididunt ut labore et dolore magna aliqua. Lorem ipsum dolor sit amet, consectetur adipisicing elit, sed do eiusmod tempor incididunt ut labore et dolore magna aliqua.</p>
<div class="abs meta" style="left:101px;top:2255px">
  <span class="count">25</span><a>comments</a>
  <span class="tags">Tags: <a>Italy</a>, <a>Best Beer</a>, <a>Spirit</a>, <a>World championship</a>, <a>Eat</a></span>
  <span class="share">Share: <span class="sq" style="background:#3b5a9a"></span><span class="sq" style="background:#3fa9d6"></span></span>
</div>

<!-- sidebar -->
<h3 class="abs side-title" style="left:844px;top:1200px">Subscribe</h3>
<div class="abs subscribe">subscribe@velmontbrew.com
  <svg width="18" height="14" viewBox="0 0 18 14"><rect x="0" y="0" width="18" height="14" fill="#7a1a2c"/><polyline points="0,0 9,8 18,0" fill="none" stroke="#fff" stroke-width="1.5"/></svg>
</div>
<div class="abs social" style="left:838px;top:1332px"><div class="box" style="background:#3b5a9a"></div><div class="num">10,500</div></div>
<div class="abs social" style="left:918px;top:1332px"><div class="box" style="background:#3fa9d6"></div><div class="num">10,500</div></div>
<div class="abs social" style="left:999px;top:1332px"><div class="box" style="background:#f08a24"></div><div class="num">10,500</div></div>

<h3 class="abs side-title" style="left:844px;top:1424px">Most popular now</h3>
<div class="abs popular">
  <a>Vineyards &amp; Winery Offers Indulgent Adventures</a>
  <a>When the Internet Actually Works</a>
  <a>Ninth Annual Petite Sirah Symposium to Have Live Broadcast</a>
  <a>Vineyards &amp; Winery Offers Indulgent Adventures</a>
  <a>When the Internet Actually Works</a>
  <a>Ninth Annual Petite Sirah Symposium to Have Live Broadcast</a>
</div>

<h3 class="abs side-title" style="left:848px;top:1730px">Beer tips &amp; tricks</h3>
<svg class="abs bubble-tail" width="40" height="40" viewBox="0 0 40 40"><polygon points="2,0 36,30 14,36" fill="#1a1a1a"/></svg>
<div class="abs bubble">
  <p>Lorem ipsum dolor sit amet, consectetur adipisicing elit, sed do eiusmod tempor incididunt ut labore.</p>
  <hr>
  <a>Read More</a>
</div>

<!-- footer -->
<div class="abs footer-rule"></div>
<div class="abs footer-brand"><span class="brand-dot" style="width:16px;height:16px"></span>Velmont
  <span class="sq" style="width:16px;height:16px;background:#3b5a9a;margin-left:6px"></span><span class="sq" style="width:16px;height:16px;background:#3fa9d6"></span></div>

<div class="abs footer-col" style="left:385px">
  <h4>NAVIGATION</h4><a>Main page</a><a>Beer examples</a><a>Tasting</a>
</div>
<div class="abs footer-col" style="left:561px">
  <h4>OTHER BEVERAGE</h4><a>More English world</a><a>And English Queen</a><a>English Tea</a><a>English beer</a>
</div>
<div class="abs footer-col" style="left:757px">
  <h4>BEER PACK</h4><a>Main page</a><a>Beer examples</a><a>Tasting</a>
</div>
<div class="abs footer-col" style="left:904px">
  <h4>OTHER LINK</h4><a>More English world</a><a>And English Queen</a><a>English Tea</a><a>English beer</a>
</div>

</body>
</html>
```